Yacht, Boats, Watersports company needs a redesign of business card

Hello Designers!
We are a Boat dealership company that sells fun in the water, we sell boats, Yachts, Kayaks and also yacht WaterSport toys. We are looking to redesign our business cards in to something a little bit more sophisticated. in a way that we can make better use of our company colors. I'm attaching a zipped file containing the company 3 sets of company logo which one is an horizontal another one is a vertical and also a chromed 3d logo. Also is included two set of business cards that we use and also some designs that i think it's interesting. We use PMS 2026c Orange and PMS 7687C Blue. I would like to see at least two different options with the orange as accent and also using blue as an accent color. It's really important for the business cards to have a font option and size that is legible to most people. Our current website is wwww.corvellamarine.com. Please visit if you want to have a better feeling of the Boat dealership
You can send Single sided or double side options. We are now using single sided but we may be open for a double side option if we really like the design.
Target Market(s)
Marine, boat sales, yacht sales, water toys sales/
Contact Information for Business Card
Name: Dale Pritchett
Address: 718 West Halden Lane,
Keel Harbor, SC 29401
Phone: 954-382-7146
Fax: 954:382-7139
Cell: 954-451-8320
Email: 212@corvellamarine.com
Website: corvellamarine.com
Requirements
Must have
- the current information of the business card provided.
logo
use the PMS Colors
Nice to have
- a touch of elegance and sophistication but simple
Should not have
- should not have any typography that is hard to read, the card should be simple but yet sophisticated.

```html
<!DOCTYPE html>
<html lang="en">
<head>
<meta charset="utf-8">
<title>Corvella Marine – Business Card</title>
<link rel="stylesheet" href="https://fonts.googleapis.com/css2?family=Poppins:wght@500;600;700&display=swap">
<style>
  :root {
    --brand-blue: #124b7d;
    --brand-blue-deep: #0e3f6a;
    --brand-navy-text: #1b4a7c;
    --brand-orange: #f26430;
    --card-white: #ffffff;
    --backdrop: #3a3735;
  }
  * { margin: 0; padding: 0; box-sizing: border-box; }
  html, body {
    width: 1200px; height: 900px; overflow: hidden;
    background: var(--backdrop);
    font-family: "Poppins", sans-serif;
  }
  .card {
    position: absolute; left: 128px; top: 167px;
    width: 944px; height: 566px;
    background: var(--card-white);
    overflow: hidden;
  }
  .brand {
    position: absolute; left: 62px; top: 65px;
    display: flex; align-items: center; gap: 14px;
  }
  .brand-ring {
    width: 94px; height: 94px; border-radius: 50%;
    border: 7px solid var(--brand-orange);
  }
  .brand-name {
    font-weight: 700; font-size: 26px; letter-spacing: 2.5px;
    color: var(--brand-blue); text-transform: uppercase;
  }
  .halftone-area {
    position: absolute; left: 40px; top: 228px;
    width: 310px; height: 72px;
    background: radial-gradient(ellipse at 40% 100%, rgba(242,100,48,.55) 0%, rgba(242,100,48,.18) 45%, rgba(242,100,48,0) 75%);
  }
  .personal {
    position: absolute; left: 584px; top: 178px;
  }
  .personal-row { display: flex; align-items: center; gap: 23px; }
  .personal-row svg { width: 22px; height: 30px; flex: none; }
  .person-name {
    font-weight: 600; font-size: 36px; color: var(--brand-navy-text); line-height: 50px;
  }
  .cell-number {
    font-weight: 600; font-size: 22px; color: var(--brand-navy-text); line-height: 40px;
    letter-spacing: .5px;
  }
  .personal-rule {
    position: absolute; left: 577px; top: 296px; width: 367px; height: 4px;
    background: var(--brand-orange);
  }
  .band {
    position: absolute; left: 0; top: 300px; width: 944px; height: 266px;
    background: var(--brand-blue);
  }
  .band-footer {
    position: absolute; left: 0; top: 517px; width: 944px; height: 49px;
    background: var(--brand-blue-deep);
  }
  .contact-tab { position: absolute; left: 0; height: 34px; }
  .contact-text {
    position: absolute; left: 178px; color: var(--card-white);
    font-weight: 500; letter-spacing: .5px;
  }
  .contact-text.phone { font-size: 23px; }
  .contact-text.email { font-size: 17px; }
  .address {
    position: absolute; left: 584px; top: 362px;
    display: flex; gap: 23px; color: var(--card-white);
  }
  .address p { font-weight: 600; font-size: 17.5px; line-height: 23px; }
  .web-bar { position: absolute; left: 540px; top: 447px; width: 404px; height: 35px; }
  .web-text {
    position: absolute; left: 629px; top: 449px; line-height: 30px;
    font-weight: 600; font-size: 19px; color: var(--card-white);
  }
</style>
</head>
<body>
<main class="card">
  <div class="brand">
    <div class="brand-ring"></div>
    <span class="brand-name">Corvella Marine</span>
  </div>

  <div class="halftone-area" role="img" aria-label="Orange halftone dot pattern fading upward"></div>

  <section class="personal">
    <div class="personal-row">
      <svg viewBox="0 0 22 30" fill="none" stroke="#f26430" stroke-width="2">
        <circle cx="11" cy="9" r="6"/>
        <path d="M2 27 v-3 a7 7 0 0 1 7-7 h4 a7 7 0 0 1 7 7 v3 z"/>
      </svg>
      <h1 class="person-name">Dale Pritchett</h1>
    </div>
    <div class="personal-row">
      <svg viewBox="0 0 22 30" fill="none" stroke="#f26430" stroke-width="2">
        <rect x="3" y="1" width="16" height="28" rx="2"/>
        <line x1="3" y1="24" x2="19" y2="24"/>
        <line x1="9" y1="4.5" x2="13" y2="4.5"/>
      </svg>
      <span class="cell-number">954-451-8320</span>
    </div>
  </section>
  <div class="personal-rule"></div>

  <div class="band"></div>
  <div class="band-footer"></div>

  <svg class="contact-tab" style="top:356px" width="162" height="34" viewBox="0 0 162 34">
    <polygon points="0,0 162,0 150,34 0,34" fill="#f26430"/>
    <path d="M69 9 l4 -1 2 5 -3 2 a10 10 0 0 0 5 5 l2 -3 5 2 -1 4 c-8 1 -15 -6 -14 -14z" fill="none" stroke="#fff" stroke-width="1.5" stroke-linejoin="round"/>
  </svg>
  <svg class="contact-tab" style="top:402px" width="148" height="34" viewBox="0 0 148 34">
    <polygon points="0,0 148,0 136,34 0,34" fill="#f26430"/>
    <g fill="none" stroke="#fff" stroke-width="1.5">
      <rect x="64" y="10" width="20" height="16" rx="1.5"/>
      <rect x="66" y="12" width="4" height="12"/>
      <rect x="73" y="6" width="8" height="6"/>
      <line x1="73" y1="16" x2="81" y2="16"/><line x1="73" y1="19" x2="81" y2="19"/><line x1="73" y1="22" x2="81" y2="22"/>
    </g>
  </svg>
  <svg class="contact-tab" style="top:447px" width="134" height="34" viewBox="0 0 134 34">
    <polygon points="0,0 134,0 122,34 0,34" fill="#f26430"/>
    <g fill="none" stroke="#fff" stroke-width="1.5" stroke-linejoin="round">
      <rect x="64" y="9" width="22" height="16" rx="1.5"/>
      <path d="M64 10 l11 8 11 -8"/>
    </g>
  </svg>

  <span class="contact-text phone" style="top:360px">954-382-7146</span>
  <span class="contact-text phone" style="top:404px">954-382-7139</span>
  <span class="contact-text email" style="top:454px">212@corvellamarine.com</span>

  <div class="address">
    <svg width="22" height="24" viewBox="0 0 22 24" fill="none" stroke="#f26430" stroke-width="1.6" style="margin-top:5px">
      <path d="M11 15 c-4 -5 -6 -7 -6 -10 a6 6 0 0 1 12 0 c0 3 -2 5 -6 10z"/>
      <circle cx="11" cy="5" r="2"/>
      <path d="M5 14 h-3 l-2 9 h22 l-2 -9 h-3"/>
    </svg>
    <div>
      <p>718 West Halden Lane,</p>
      <p>Keel Harbor, SC 29401</p>
    </div>
  </div>

  <svg class="web-bar" viewBox="0 0 404 35">
    <polygon points="0,0 404,0 404,35 12,35" fill="#f26430"/>
    <g fill="none" stroke="#fff" stroke-width="1.5">
      <circle cx="55" cy="17.5" r="9"/>
      <ellipse cx="55" cy="17.5" rx="4" ry="9"/>
      <line x1="46" y1="17.5" x2="64" y2="17.5"/>
    </g>
  </svg>
  <span class="web-text">corvellamarine.com</span>
</main>
</body>
</html>
```